Consulting company needs Business Cards - rough concept provided

I'm looking for someone to take our business card idea and make is slick and polished - to communicate our high-end, sophisticated, serious consulting business. We have a rough layout we did in-house. We are open to ideas on repo-ing elements, adjusting sizes, typefaces etc... within the general concept we've already come up with. We want it to be super-clean and sophisticated. We want to keep the white backgrounds, and blue brand colors. Our goal is to print with painted blue edges on thick cardstock. Thank you!!

```html
<!DOCTYPE html>
<html lang="en">
<head>
<meta charset="utf-8">
<title>Kelvane Stationery</title>
<link rel="stylesheet" href="https://fonts.googleapis.com/css2?family=Open+Sans:wght@400;600;700;800&display=swap">
<style>
  :root {
    --brand-blue: #1a8ad4;
    --brand-blue-deep: #0f76bd;
    --line-blue: #4aa3df;
    --grid-tint: #dcecf8;
    --ink: #1d1d1f;
    --muted: #8a8a8a;
    --paper: #ffffff;
    --backdrop: #ecebe8;
    --block-grey: #e4e4e4;
    --block-grey-light: #efefef;
  }
  * { box-sizing: border-box; margin: 0; padding: 0; }
  html, body { width: 1200px; height: 1200px; overflow: hidden; }
  body {
    background: var(--backdrop);
    font-family: "Open Sans", Arial, sans-serif;
    color: var(--ink);
    position: relative;
  }
  .sheet {
    position: absolute;
    background: var(--paper);
    overflow: hidden;
    box-shadow: 0 0 0 1px rgba(0,0,0,0.05);
  }
  .sheet svg.decor { position: absolute; inset: 0; width: 100%; height: 100%; }
  .brand-name {
    position: absolute;
    font-weight: 800;
    color: var(--brand-blue);
    letter-spacing: 0.01em;
    line-height: 1;
    white-space: nowrap;
  }
  .pattern-fill { position: absolute; background: linear-gradient(135deg, var(--grid-tint), #eef6fc); }

  /* Letterhead */
  .letterhead { left: 129px; top: 127px; width: 574px; height: 778px; }
  .letterhead .brand-name { left: 32px; top: 34px; font-size: 74px; }
  .letter-body { position: absolute; left: 162px; top: 170px; width: 330px; font-size: 11px; line-height: 14px; }
  .letter-body .sender { font-weight: 700; font-size: 11.5px; }
  .letter-body .sub { color: var(--muted); }
  .letter-body p { margin-top: 14px; }
  .letter-body .gap { margin-top: 58px; }

  /* Business cards */
  .card { width: 288px; height: 172px; left: 773px; }
  .card-front { top: 146px; }
  .card-front .brand-name { left: 28px; top: 72px; font-size: 34px; }
  .card-back { top: 340px; }
  .card-back .label { position: absolute; left: 32px; top: 26px; font-size: 10.5px; font-weight: 700; }
  .card-back .label span { display: block; font-weight: 400; color: var(--muted); font-size: 9.5px; }
  .contact { position: absolute; left: 134px; top: 72px; font-size: 10px; line-height: 13px; }
  .contact .name { font-weight: 700; font-size: 10.5px; }

  /* Envelope front */
  .envelope-front { left: 495px; top: 490px; width: 568px; height: 266px; }
  .envelope-front .return { position: absolute; left: 56px; top: 64px; font-size: 11px; line-height: 14px; }
  .envelope-front .return .sender { font-weight: 700; }
  .envelope-front .brand-name { left: 54px; top: 200px; font-size: 42px; }

  /* Envelope back */
  .envelope-back { left: 495px; top: 799px; width: 568px; height: 268px; }
  .seal { position: absolute; left: 251px; top: 47px; width: 64px; height: 60px; background: var(--brand-blue); }
</style>
</head>
<body>

<section class="sheet letterhead" aria-label="Letterhead">
  <div class="pattern-fill" style="left:91px; top:616px; width:450px; height:162px;" role="img" aria-label="Light blue grid pattern"></div>
  <div class="pattern-fill" style="left:82px; top:675px; width:90px; height:103px;" role="img" aria-label="Small blue grid pattern"></div>
  <svg class="decor" viewBox="0 0 574 778" aria-hidden="true">
    <g stroke="var(--line-blue)" stroke-width="1" fill="none">
      <line x1="33" y1="0" x2="33" y2="505"/>
      <line x1="0" y1="96" x2="574" y2="96"/>
      <line x1="540" y1="0" x2="540" y2="616"/>
      <line x1="551" y1="0" x2="551" y2="34"/>
      <line x1="530" y1="22" x2="574" y2="22"/>
    </g>
    <polygon points="0,484 35,488 91,570 91,778 0,778" fill="var(--brand-blue)"/>
  </svg>
  <div class="brand-name">KELVANE</div>
  <div class="letter-body">
    <div class="sender">KELVANE</div>
    <div class="sub">Sample address name</div>
    <div class="sub">Sample School</div>
    <p style="margin-top:34px">Dear Maxiam,</p>
    <p>Lorem ipsum dolor sit amet, consectetur adipiscing elit, sed do eiusmod tempor incididunt ut labore et dolore magna aliqua. Ut enim ad minim veniam, quis nostrud exercitation ullamco laboris nisi ut aliquip ex ea commodo consequat.</p>
    <p>Lorem ipsum dolor sit amet, consectetur adipiscing elit, sed do eiusmod tempor incididunt ut labore et dolore magna aliqua. Ut enim ad minim veniam, quis nostrud ex ea commodo consequat.</p>
    <p>Duis aute irure dolor in reprehenderit in voluptate velit esse cillum dolore eu fugiat nulla pariatur sunt in culpa commodo consequat.</p>
    <p class="gap">Yours sincerely,</p>
    <div>Lorem ipsum dolor sit amet</div>
    <div class="sub">Sample team</div>
  </div>
</section>

<section class="sheet card card-front" aria-label="Business card front">
  <div class="pattern-fill" style="left:6px; top:120px; width:88px; height:52px;" role="img" aria-label="Small blue grid pattern"></div>
  <svg class="decor" viewBox="0 0 288 172" aria-hidden="true">
    <g stroke="var(--line-blue)" stroke-width="1" fill="none">
      <line x1="0" y1="12" x2="288" y2="12"/>
      <line x1="246" y1="0" x2="246" y2="140"/>
      <line x1="262" y1="0" x2="262" y2="60"/>
      <line x1="240" y1="118" x2="288" y2="118"/>
      <line x1="20" y1="0" x2="20" y2="172"/>
    </g>
  </svg>
  <div class="brand-name">KELVANE</div>
</section>

<section class="sheet card card-back" aria-label="Business card back">
  <svg class="decor" viewBox="0 0 288 172" aria-hidden="true">
    <rect x="128" y="17" width="140" height="38" fill="var(--block-grey)"/>
    <rect x="50" y="60" width="22" height="112" fill="var(--block-grey-light)"/>
    <rect x="78" y="60" width="14" height="112" fill="var(--block-grey)"/>
    <g stroke="#c9c9c9" stroke-width="1" fill="none">
      <line x1="0" y1="60" x2="288" y2="60"/>
      <line x1="120" y1="0" x2="120" y2="172"/>
      <line x1="0" y1="150" x2="120" y2="150"/>
    </g>
  </svg>
  <div class="label">BUSINESS CARD<span>Project back</span></div>
  <div class="contact">
    <div class="name">KELVANE</div>
    <div>Kelvane.com</div>
    <div>+123 555 0142</div>
    <div>info@kelvane.com</div>
    <div>www.kelvane.com</div>
  </div>
</section>

<section class="sheet envelope-front" aria-label="Envelope front">
  <div class="pattern-fill" style="left:39px; top:0; width:440px; height:48px;" role="img" aria-label="Light blue grid band"></div>
  <svg class="decor" viewBox="0 0 568 266" aria-hidden="true">
    <g stroke="var(--line-blue)" stroke-width="1" fill="none">
      <line x1="0" y1="234" x2="568" y2="234"/>
      <line x1="540" y1="190" x2="540" y2="266"/>
    </g>
    <polygon points="0,119 39,190 39,266 0,266" fill="var(--brand-blue)"/>
    <polygon points="468,14 568,14 568,186 505,126 505,50" fill="var(--brand-blue)"/>
  </svg>
  <div class="return">
    <div class="sender">KELVANE</div>
    <div>Sample Return Name</div>
    <div>Sample 00000</div>
  </div>
  <div class="brand-name">KELVANE</div>
</section>

<section class="sheet envelope-back" aria-label="Envelope back">
  <svg class="decor" viewBox="0 0 568 268" aria-hidden="true">
    <polyline points="0,2 26,60 540,66 566,2" fill="none" stroke="#d6d6d6" stroke-width="1.5"/>
    <line x1="0" y1="266" x2="200" y2="140" stroke="#e6e6e6"/>
    <line x1="568" y1="266" x2="368" y2="140" stroke="#e6e6e6"/>
  </svg>
  <div class="seal"></div>
</section>

</body>
</html>
```